professional coaching community needs new look for website

We require a website design that attracts professionals. We run a large, global professional coaching community (e.g. executive, business, personal coaches NOT sports coaches). Our members are committed to their professional and personal development and they enjoy building relationships with other coaches across the world. We also champion the success of coaches and the coaching industry by providing business support resources to our members. We do not mind which colours you use, but whatever the combination, the combinations must be professional and refined. It would be good to have some of the familiarity of the old site colours, with some new, more professional element. We have a number of requirements for the homepage and members design, and this is attached.

Reason: I am extending the deadline for this design, in order to give feedback and see how current designs can be tweaked.

Target Market(s)

Here are some ideas for images, which gives and idea of the target market also:

Ideas for website images:

1. http://www.pixelvarno.com/stock-photo-48213077-business-success.php?st=4b2a918 (I like the people in this one – they seem very dynamic and a good mix of women and men)
2. http://www.pixelvarno.com/stock-photo-51729406-business-communications.php?st=4b2a918 (I like all of the speech bubbles in this one, that’s what the MentraLoop community does – pairs up in two’s or small groups and engages in professional talking)
3. http://www.pixelvarno.com/stock-photo-37086152-global-business-working.php?st=4b2a918 (I like the combination of the world and the people talking in different groups)
4. http://www.pixelvarno.com/stock-photo-44861039-global-business-people.php?st=e512604 (I like the world in this one – would be good to see combination of world and #1 dynamic people, which is the MentraLoop community)

Industry/Entity Type

Building

Requirements
Must have
• See attached uploaded files including homepage design, member dashboard design, and example profile (profiles need to be included him banner design). Note that any text must not be build into graphic. It needs to be able to be edited via html.

```html
<!DOCTYPE html>
<html lang="en">
<head>
<meta charset="utf-8">
<title>MentraLoop – Coaching Community</title>
<link href="https://fonts.googleapis.com/css2?family=Open+Sans:ital,wght@0,400;0,600;0,700;1,400&display=swap" rel="stylesheet">
<style>
:root{
  --navy:#2d4a6a;
  --navy-dark:#22364d;
  --green:#7cb342;
  --green-dark:#5f9a2c;
  --text:#555c63;
  --muted:#8a9096;
  --page:#e8ebee;
  --panel:#ffffff;
  --line:#d6dadf;
  --footer:#2b2e33;
  --footer-text:#9aa0a6;
  --link:#3b7cc4;
}
*{box-sizing:border-box;margin:0;padding:0}
html,body{width:896px;height:1200px;overflow:hidden}
body{font-family:"Open Sans",Arial,sans-serif;color:var(--text);background:var(--page);position:relative}
.site-header{position:absolute;top:0;left:0;width:896px;height:42px;background:#fff;border-bottom:1px solid var(--line)}
.brand{position:absolute;left:40px;top:8px;display:flex;align-items:center;gap:7px;font-weight:700;font-size:22px;color:var(--navy);letter-spacing:-.3px}
.brand-dot{width:14px;height:14px;border-radius:50%;background:var(--green)}
.main-nav{position:absolute;right:40px;top:0;display:flex;height:42px;align-items:center;font-size:11px}
.main-nav a{color:var(--navy);text-decoration:none;padding:0 10px;height:42px;line-height:42px}
.main-nav a.active{background:var(--green);color:#fff}
.main-nav a.login{background:var(--navy-dark);color:#fff;height:22px;line-height:22px;margin-left:8px;border-radius:2px}
.hero{position:absolute;top:42px;left:0;width:896px;height:330px;background:linear-gradient(180deg,#d5e4ef 0%,#eef3f7 55%,#c7d6e2 100%);overflow:hidden}
.hero-globe{position:absolute;left:-60px;top:40px;width:700px;height:420px;border-radius:50%;background:radial-gradient(ellipse at 45% 30%,#f4f7fa 0%,#d8e3ec 50%,#b9cad8 100%);opacity:.9}
.hero h1{position:absolute;left:100px;top:95px;width:380px;font-size:25px;line-height:31px;font-weight:600;color:var(--navy)}
.btn-connect{position:absolute;left:100px;top:185px;background:var(--navy-dark);color:#fff;font-size:11px;padding:8px 14px;border-radius:2px}
.portrait-card{position:absolute;left:590px;top:25px;width:150px;height:205px;background:#fff;padding:6px;box-shadow:0 2px 6px rgba(0,0,0,.18)}
.portrait-photo{width:138px;height:165px;background:linear-gradient(160deg,#d9c7b5,#8a7464 60%,#4d4a4c)}
.portrait-name{font-size:11px;font-style:italic;color:var(--navy);text-align:center;margin-top:8px}
.left-col{position:absolute;left:40px;top:380px;width:540px}
.why-box{background:var(--panel);border:1px solid var(--line);height:96px}
.why-box h2{font-size:12px;font-weight:600;color:var(--navy);text-align:center;background:#f2f4f6;border-bottom:1px solid var(--line);padding:6px 0}
.benefits{display:grid;grid-template-columns:repeat(3,1fr);padding:8px 30px;row-gap:4px;font-size:10px;list-style:none}
.benefits li::before{content:"• ";color:var(--navy)}
.video{margin-top:10px;height:228px;background:#1d1f22;position:relative}
.video-bar{height:20px;background:#2f3236;color:#cfd3d7;font-size:9px;line-height:20px;padding-left:8px}
.video-still{position:absolute;top:20px;left:0;right:0;bottom:18px;background:radial-gradient(ellipse at 30% 60%,#5d6a73 0%,#2d3439 55%,#15181b 100%)}
.video-play{position:absolute;left:244px;top:92px}
.video-controls{position:absolute;bottom:0;left:0;right:0;height:18px;background:#0f1113}
.video-progress{position:absolute;left:30px;right:60px;top:8px;height:3px;background:#444}
.video-progress span{display:block;width:12%;height:3px;background:#c33}
.article{margin-top:12px;font-size:10px;line-height:15px}
.article h3{color:var(--green-dark);font-size:14px;font-weight:600;margin-bottom:6px}
.article p{margin-bottom:8px}
.article a{color:var(--link);text-decoration:none}
.right-col{position:absolute;left:592px;top:354px;width:268px}
.signin{background:var(--panel);border:1px solid var(--line)}
.signin h2{background:var(--green);color:#fff;font-size:14px;font-weight:600;text-align:center;padding:7px 0}
.perks{list-style:none;padding:10px 14px 6px;font-size:10px;line-height:13px}
.perks li{display:flex;gap:6px;margin-bottom:6px}
.perks svg{flex:none;margin-top:1px}
.signin-form{background:#f1f3f5;border-top:1px solid var(--line);padding:10px 14px 12px;font-size:9.5px}
.field{display:flex;align-items:center;margin-bottom:6px}
.field span{width:70px}
.field i{flex:1;height:18px;background:#fff;border:1px solid var(--line)}
.terms{display:flex;gap:5px;align-items:flex-start;margin:6px 0 8px;line-height:12px}
.terms b{flex:none;width:9px;height:9px;border:1px solid #999;background:#fff;margin-top:1px}
.btn-signup{display:block;margin:0 auto;width:100px;text-align:center;background:var(--green);color:#fff;font-size:10px;padding:5px 0;border-radius:2px}
.ad-box{margin-top:22px;height:135px;background:#c9cdd2;display:flex;align-items:center;justify-content:center;color:#8c9399;font-size:10px}
.social{display:flex;justify-content:center;gap:6px;margin-top:12px}
.social i{width:14px;height:14px;border-radius:50%;background:#b9bec4}
.supporters{margin-top:10px;background:var(--panel);border:1px solid var(--line);height:140px}
.supporters h2{background:var(--green);color:#fff;font-size:12px;font-weight:600;text-align:center;padding:5px 0}
.supporter-mark{margin:10px auto 0;width:70px;height:24px;border-radius:12px;background:#f18b21}
.supporter-mark.second{width:44px;height:28px;border-radius:4px;background:#d8352f}
.supporters p{text-align:center;font-size:8px;color:#c0392b;margin-top:8px}
.site-footer{position:absolute;left:0;top:1044px;width:896px;height:156px;background:var(--footer);color:var(--footer-text);font-size:8.5px}
.footer-top{position:absolute;left:40px;right:40px;top:28px;display:flex;justify-content:space-between}
.footer-links{display:flex;gap:18px}
.footer-contact{display:flex;gap:22px}
.footer-rule{position:absolute;left:40px;right:40px;top:60px;border-top:1px solid #3e4248}
.footer-bottom{position:absolute;left:40px;right:40px;top:76px;display:flex;justify-content:space-between;align-items:center}
.footer-social{display:flex;gap:8px}
.footer-social i{width:12px;height:12px;background:#5a5f66;border-radius:2px}
</style>
</head>
<body>
<header class="site-header">
  <div class="brand"><span class="brand-dot"></span>MentraLoop</div>
  <nav class="main-nav">
    <a class="active">Home</a><a>Join Us</a><a>Coaching</a><a>Mentoring</a><a>Supervision</a><a>Resources</a><a class="login">Login</a>
  </nav>
</header>

<section class="hero">
  <div class="hero-globe" role="img" aria-label="Soft globe and sky backdrop"></div>
  <h1>Join the most dinamic coaching community in the world</h1>
  <span class="btn-connect">Connect with Coach</span>
  <figure class="portrait-card">
    <div class="portrait-photo" role="img" aria-label="Portrait photo of a featured coach"></div>
    <figcaption class="portrait-name">Maren Holloway</figcaption>
  </figure>
</section>

<main class="left-col">
  <section class="why-box">
    <h2>Why are there XXXX MentraLoops?</h2>
    <ul class="benefits">
      <li>Benefit 1</li><li>Benefit 1</li><li>Benefit 1</li>
      <li>Benefit 2</li><li>Benefit 2</li><li>Benefit 2</li>
      <li>Benefit 3</li><li>Benefit 3</li><li>Benefit 3</li>
    </ul>
  </section>
  <section class="video">
    <div class="video-bar">Coaching Day Film</div>
    <div class="video-still" role="img" aria-label="Video still of a world map at dusk"></div>
    <svg class="video-play" width="52" height="36" viewBox="0 0 52 36"><rect width="52" height="36" rx="8" fill="rgba(0,0,0,.7)"/><path d="M21 10 L34 18 L21 26 Z" fill="#fff"/></svg>
    <div class="video-controls"><div class="video-progress"><span></span></div></div>
  </section>
  <article class="article">
    <h3>Not Too Long Header</h3>
    <p>Lorem ipsum dolor sit amet, consectetur adipiscing elit. Aenean commodo ligula eget dolor. Aenean massa. Cum sociis natoque penatibus et magnis dis parturient montes, nascetur ridiculus mus. Donec quam felis, ultricies nec, pellentesque eu, pretium quis, sem. Nulla consequat massa quis enim. Donec pede justo, fringilla vel, aliquet nec, vulputate eget, arcu. In enim justo, rhoncus ut, imperdiet a, venenatis vitae, justo. Nullam dictum felis eu pede mollis pretium. Integer tincidunt. Cras dapibus.</p>
    <p><a>Vivamus elementum semper nisi.</a> Aenean vulputate eleifend tellus. Aenean leo ligula, porttitor eu, consequat vitae, eleifend ac, enim. Aliquam lorem ante, dapibus in, viverra quis, feugiat a, tellus. Phasellus viverra nulla ut metus varius laoreet. Quisque rutrum. Aenean imperdiet. Etiam ultricies nisi vel augue. Curabitur ullamcorper ultricies nisi. Nam eget dui.</p>
  </article>
</main>

<aside class="right-col">
  <section class="signin">
    <h2>Quick Signin</h2>
    <ul class="perks">
      <li><svg width="10" height="10" viewBox="0 0 10 10"><path d="M1 5 L4 8 L9 2" stroke="#7cb342" stroke-width="2" fill="none"/></svg>Free to Join</li>
      <li><svg width="10" height="10" viewBox="0 0 10 10"><path d="M1 5 L4 8 L9 2" stroke="#7cb342" stroke-width="2" fill="none"/></svg>3 Issues of Coaching Research in Practice</li>
      <li><svg width="10" height="10" viewBox="0 0 10 10"><path d="M1 5 L4 8 L9 2" stroke="#7cb342" stroke-width="2" fill="none"/></svg>Monthly Issues of Lessons from the Field</li>
      <li><svg width="10" height="10" viewBox="0 0 10 10"><path d="M1 5 L4 8 L9 2" stroke="#7cb342" stroke-width="2" fill="none"/></svg>Access to our community</li>
      <li><svg width="10" height="10" viewBox="0 0 10 10"><path d="M1 5 L4 8 L9 2" stroke="#7cb342" stroke-width="2" fill="none"/></svg>Online profile</li>
    </ul>
    <form class="signin-form">
      <div class="field"><span>First Name</span><i></i></div>
      <div class="field"><span>Last Name</span><i></i></div>
      <div class="field"><span>Email</span><i></i></div>
      <div class="terms"><b></b>I have read the MentraLoop Terms and Conditions</div>
      <span class="btn-signup">Sign Up Now</span>
    </form>
  </section>
  <div class="ad-box">Ads</div>
  <div class="social"><i></i><i></i><i></i></div>
  <section class="supporters">
    <h2>Thanks to our Supporters</h2>
    <div class="supporter-mark" role="img" aria-label="Supporter badge"></div>
    <div class="supporter-mark second" role="img" aria-label="Supporter badge"></div>
    <p>See more of our supporters</p>
  </section>
</aside>

<footer class="site-footer">
  <div class="footer-top">
    <nav class="footer-links"><span>Home</span><span>About</span><span>Blog</span><span>Contact</span><span>Privacy</span></nav>
    <div class="footer-contact"><span>+44 (0)20 7946 0381</span><span>hello@mentraloop.com</span></div>
  </div>
  <div class="footer-rule"></div>
  <div class="footer-bottom">
    <span>© 2013 MentraLoop. All rights reserved. Legal Notice</span>
    <div class="footer-social"><i></i><i></i><i></i><i></i><i></i></div>
  </div>
</footer>
</body>
</html>
```